website for local kavenda practicioner and yoga teacher trainer

The website should function primarily as:
A place where people can discover Kavenda and book sessions.
A central hub connecting all of my work.
A professional home that reflects my personality and approach.
Website design for Liesbet Oonwerk — Kavenda® Structural Integration practitioner, movement educator, yoga teacher and teacher trainer.
A website that can grow with future projects.
The website should feel: Warm, Human, Invitational, Professional, Accessible, Intelligent, Calm, Clear, Playful, Exploratory, Trustworthy
Avoid: New age aesthetics, Mystical clichés, Excessive spirituality, ”Guru" vibes, Overly clinical design, Corporate wellness branding, Busy layouts
Think: modern, grounded, curious and real.
My work combines three interconnected areas:
1.Bodywork: Touch, structure, awareness and one-on-one support.
2. Movement: Yoga, Pilates and embodied movement.
3. Education: Teacher trainings, workshops and continued learning.
Underlying values:
Curiosity over certainty
Possibility over perfection
Complexity without overwhelm
Science and lived experience together
Exploration rather than dogma
Human beings before methods
The primary goal of the website is to introduce people to Kavenda® Structural Integration and make it easy for them to:
Understand what Kavenda is
Discover whether it might be relevant for them
Learn what to expect from a session
Book an appointment
Booking should always feel visible and easy.
Secondary Goal: Present all other aspects of my work in one coherent place:
Yoga classes
Pilates classes
Teacher trainings
Workshops
Retreats
One-on-one movement sessions
Collaborations with studios
Website Structure
1: HOME
1.1.Hero Section: Large welcoming image
1.2 Two Main Pathways
- Bodywork: Kavenda® Structural Integration
- Movement & Education: Yoga, Pilates, trainings, workshops and retreats
- About Preview: Small introduction with portrait. + Button:
Read More
1.3 Current Events / What's Coming Up: Upcoming trainings, workshops and retreats. (This section should be easy to update)
1.4. Contact / Newsletter: Simple contact information
2: Kavenda® Structural Integration
What is Kavenda?
For whom is it?
What does a session look like?
FAQ
Prices
Booking
Future possibility:
Kaven Movement sessions
3: Movement
- Introductory text.
- Studio Classes (link to “my home base” - > local yoga studio)
- One-to-One Sessions: booking option (this is small; not a key aspect I want to promote)
- Workshops/ Retreats / Teacher Trainings => This section should be flexible and easy to update. Visitors should be able to click into specific offerings.
4. Events
Dynamic page for: Teacher trainings, Retreats, Workshops (see section in movement; here more elaborate)
Each event should contain: Image, Short description, Location, Date, Button for more information. (Linking to hosting studio/location)
5. Work With Me
For studios, organisations and teacher training schools.
Examples: Guest teaching, Workshops, Anatomy, Sequencing, Teacher development , Continuing education -> Clear call-to-action.
Call to action!!=> Book a Session
Prominent button in the navigation.
Footer:
- About Me: Longer biography (6th page)
Personal story and background.
- Testimonials (7th page): Separate page containing testimonials from:
Kavenda clients
Students
Teacher trainees
- Contact: 8th page
Visual Direction
Natural textures. Lots of white space.Editorial feeling.Professional photography.Simple navigation.
Less "wellness influencer.” More:Thoughtful, Contemporary, Timeless, Grounded, Human
Photography should show:
Teaching
Hands-on work
Natural movement
Real interaction
Simplicity
Avoid stereotypical yoga imagery and overly spiritual aesthetics.
Keywords
Warm. Curious. Human. Professional. Embodied. Intelligent. Accessible. Playful. Grounded. Exploratory. Real.
Inspiration / Core Message
Helping people feel more at home in their bodies through touch, movement and education.
The website should communicate that these are not separate services, but different expressions of the same intention:
Bodywork • Movement • Education.
Colours:
light orange/beige: e3d5c4
light orange/off white: f9f7f3
gray azure: 556b78
orange: d07b5a
grey orange: c09f80
dark grey: 3e3e3e
dark gray cyan 2f4f4f
gray green colour: a7c4a0
Fonts: Montserrat and Poppins + raleway
In added documents a try out idea of a website + logo. I will mainly use the logo with diffrent colours (image next to text).
My audience consists of people who want to feel more at home in their bodies and who appreciate a thoughtful, grounded and human approach to movement, touch and education. (30-65yo)
wellbeing
5+ page
- montserrat, poppins, raleway

```html
<!DOCTYPE html>
<html lang="en">
<head>
<meta charset="utf-8">
<title>Liesbet Oonwerk — Kavenda® Structural Integration &amp; Movement Education</title>
<link href="https://fonts.googleapis.com/css2?family=Montserrat:wght@400;500;600&family=Raleway:wght@400;500;600&display=swap" rel="stylesheet">
<style>
  :root {
    --orange: #d07b5a;
    --beige: #e3d5c4;
    --offwhite: #f9f7f3;
    --azure: #556b78;
    --grey-orange: #c09f80;
    --dark: #3e3e3e;
    --cyan-dark: #2f4f4f;
    --sage: #a7c4a0;
    --band: #f1edeb;
    --muted: #6b6b6b;
    --white: #ffffff;
  }
  * { box-sizing: border-box; margin: 0; padding: 0; }
  html, body { width: 1200px; height: 3582px; overflow: hidden; }
  body { background: var(--white); color: var(--dark); font-family: "Raleway", sans-serif; position: relative; }
  h1, h2, h3, h4 { font-family: "Montserrat", sans-serif; font-weight: 400; }
  a { color: inherit; text-decoration: none; }

  /* Header */
  .site-header { position: absolute; top: 0; left: 0; width: 1200px; height: 77px; display: flex; align-items: center; padding: 0 65px; background: var(--white); }
  .brand { display: flex; align-items: center; gap: 10px; font-family: "Montserrat", sans-serif; font-size: 21px; font-weight: 500; color: var(--dark); }
  .brand-dot { width: 18px; height: 18px; border-radius: 50%; background: var(--orange); }
  .main-nav { margin-left: auto; display: flex; align-items: center; gap: 27px; font-family: "Montserrat", sans-serif; font-size: 14px; font-weight: 500; color: var(--dark); }
  .main-nav .active { color: var(--orange); border-bottom: 2px solid var(--orange); padding-bottom: 4px; margin-top: 6px; }
  .btn { display: inline-flex; align-items: center; justify-content: center; border-radius: 30px; font-family: "Montserrat", sans-serif; font-weight: 600; letter-spacing: 1px; text-transform: uppercase; }
  .btn-primary { background: var(--orange); color: var(--white); }
  .btn-nav { width: 158px; height: 32px; font-size: 13px; margin-left: 0; }

  /* Hero */
  .hero { position: absolute; top: 77px; left: 0; width: 1200px; height: 660px; }
  .hero-photo { position: absolute; inset: 0; background: linear-gradient(90deg, #6d6c6a 0%, #8a8885 35%, #b9b6b2 55%, #a7a3a3 70%, #8d8fa8 100%); }
  .hero-content { position: absolute; left: 65px; top: 150px; width: 460px; color: var(--white); }
  .hero-title { font-size: 54px; line-height: 60px; font-weight: 500; letter-spacing: -1px; }
  .hero-title em { font-style: normal; color: var(--orange); }
  .hero-lead { margin-top: 34px; width: 380px; font-size: 13.5px; line-height: 23px; }
  .hero-actions { margin-top: 36px; display: flex; gap: 21px; }
  .hero-actions .btn { height: 54px; font-size: 13.5px; }
  .hero-actions .btn-primary { width: 178px; }
  .btn-ghost { width: 208px; border: 1.5px solid rgba(255,255,255,0.7); color: var(--white); }

  /* Pathways */
  .pathways { position: absolute; top: 820px; left: 65px; width: 1070px; height: 600px; }
  .pathway { position: absolute; top: 0; }
  .pathway-bodywork { left: 0; width: 500px; }
  .pathway-movement { left: 549px; width: 521px; }
  .pathway-image { height: 334px; border-radius: 14px; }
  .img-touch { background: linear-gradient(135deg, #6b3f22 0%, #b77a4d 45%, #d9a97a 70%, #8a5a3a 100%); }
  .img-studio { background: linear-gradient(180deg, #4a3d31 0%, #c9b39a 40%, #e8dccc 60%, #5b4a3b 100%); }
  .pathway h2 { margin-top: 30px; font-size: 40px; color: var(--dark); }
  .pathway p { margin-top: 14px; font-size: 13px; line-height: 20px; color: var(--muted); }
  .pathway ul { margin-top: 24px; list-style: none; font-family: "Montserrat", sans-serif; font-size: 15px; font-weight: 500; }
  .pathway li { display: flex; align-items: center; gap: 10px; line-height: 23.5px; }
  .pathway li::before { content: ""; width: 6px; height: 6px; background: var(--orange); }
  .text-link { display: inline-flex; align-items: center; gap: 6px; margin-top: 30px; font-size: 14px; color: var(--orange); }

  /* About */
  .about { position: absolute; top: 1608px; left: 65px; width: 1070px; height: 450px; }
  .about-portrait { position: absolute; left: 0; top: 0; width: 519px; height: 450px; background: linear-gradient(120deg, #3b2e24 0%, #8a7058 40%, #cfb79b 65%, #6d5644 100%); box-shadow: 0 20px 40px rgba(0,0,0,0.08); }
  .about-text { position: absolute; left: 566px; top: 25px; width: 505px; }
  .eyebrow { font-family: "Montserrat", sans-serif; font-size: 16px; color: var(--orange); }
  .about-text h2 { margin-top: 12px; font-size: 38px; line-height: 42px; color: var(--dark); width: 380px; }
  .about-text p { margin-top: 22px; font-size: 13px; line-height: 23.5px; color: var(--muted); }
  .about-text p + p { margin-top: 23px; }
  .btn-outline { margin-top: 25px; width: 174px; height: 55px; border: 1.5px solid var(--orange); color: var(--orange); font-size: 13.5px; }

  /* Events */
  .events { position: absolute; top: 2185px; left: 65px; width: 1070px; }
  .events-label { font-family: "Montserrat", sans-serif; font-size: 16px; letter-spacing: 1px; color: var(--orange); }
  .events-head { display: flex; justify-content: space-between; align-items: baseline; }
  .events-head h2 { font-size: 38px; color: var(--dark); margin-top: 4px; }
  .view-all { font-size: 14px; color: var(--muted); }
  .event-grid { position: absolute; top: 117px; left: 0; width: 1070px; }
  .event-card { position: absolute; top: 0; width: 339px; }
  .event-card:nth-child(1) { left: 0; }
  .event-card:nth-child(2) { left: 362px; }
  .event-card:nth-child(3) { left: 725px; }
  .event-image { height: 247px; border-radius: 10px; }
  .img-workshop { background: linear-gradient(180deg, #f2f0ee 0%, #e7e3de 55%, #c8a27e 100%); }
  .img-retreat { background: linear-gradient(180deg, #d9c6b2 0%, #8f9aa3 30%, #4f6a3e 65%, #2f4a26 100%); }
  .img-course { background: linear-gradient(135deg, #a9cfc6 0%, #b8d8cf 50%, #ede7dc 75%, #3a3a3a 100%); }
  .event-meta { margin-top: 22px; display: flex; align-items: center; gap: 12px; font-size: 13px; color: var(--muted); }
  .badge { font-family: "Montserrat", sans-serif; font-size: 8px; font-weight: 600; text-transform: uppercase; padding: 3px 7px; border-radius: 3px; }
  .badge-workshop { background: #f7dfd5; color: var(--orange); }
  .badge-retreat { background: #e3ebef; color: var(--azure); }
  .badge-course { background: #e6e6e6; color: var(--dark); }
  .event-card h3 { margin-top: 12px; font-size: 20px; color: var(--dark); }
  .event-card p { margin-top: 14px; font-size: 13px; line-height: 21px; color: var(--muted); width: 290px; }
  .event-status { display: block; margin-top: 12px; font-size: 13.5px; font-weight: 500; color: var(--orange); }

  /* Connect */
  .connect { position: absolute; top: 2838px; left: 0; width: 1200px; height: 414px; background: var(--band); }
  .newsletter { position: absolute; left: 153px; top: 122px; width: 420px; }
  .newsletter h2 { font-size: 26px; color: var(--dark); }
  .newsletter p { margin-top: 18px; font-size: 15px; line-height: 24px; color: var(--dark); }
  .subscribe { margin-top: 25px; display: flex; gap: 14px; }
  .subscribe input { width: 294px; height: 42px; border: 1px solid var(--grey-orange); background: var(--white); font-family: "Raleway", sans-serif; font-size: 12.5px; color: var(--muted); padding: 0; }
  .subscribe button { width: 112px; height: 42px; border: 0; background: var(--orange); color: var(--white); font-family: "Montserrat", sans-serif; font-size: 10px; font-weight: 600; letter-spacing: 0.5px; }
  .contact-card { position: absolute; left: 627px; top: 67px; width: 419px; height: 280px; background: var(--offwhite); border-radius: 10px; box-shadow: 0 6px 20px rgba(0,0,0,0.04); padding: 32px 33px; }
  .contact-card h3 { font-size: 20px; color: var(--muted); }
  .contact-card p { margin-top: 22px; font-size: 12.5px; line-height: 20px; color: var(--dark); }
  .contact-list { list-style: none; margin-top: 22px; font-size: 13px; color: var(--dark); }
  .contact-list li { display: flex; align-items: center; gap: 14px; line-height: 33px; }
  .social { margin-top: 18px; display: flex; gap: 18px; }
  .social span { width: 20px; height: 20px; border: 1.8px solid var(--dark); border-radius: 50%; }

  /* Footer */
  .site-footer { position: absolute; top: 3252px; left: 0; width: 1200px; height: 330px; }
  .footer-brand { position: absolute; left: 67px; top: 75px; }
  .footer-brand .brand { font-size: 17px; }
  .footer-brand p { margin-top: 18px; font-size: 13px; line-height: 20px; color: var(--dark); }
  .footer-col { position: absolute; top: 73px; }
  .footer-col h4 { font-size: 13px; font-weight: 500; letter-spacing: 1px; color: var(--dark); }
  .footer-col ul { list-style: none; margin-top: 12px; font-size: 13px; color: var(--muted); }
  .footer-col li { line-height: 26px; }
  .footer-pages { left: 496px; }
  .footer-locations { left: 924px; }
  .footer-locations li { line-height: 20px; }
  .copyright { position: absolute; top: 305px; width: 1200px; text-align: center; font-size: 9.5px; color: var(--dark); }
</style>
</head>
<body>

<header class="site-header">
  <a class="brand" href="#"><span class="brand-dot"></span>Liesbet Oonwerk</a>
  <nav class="main-nav">
    <a class="active" href="#">Home</a>
    <a href="#">Kavenda®</a>
    <a href="#">Movement</a>
    <a href="#">Events</a>
    <a href="#">About</a>
    <a href="#">Contact</a>
    <a class="btn btn-primary btn-nav" href="#">Book a session</a>
  </nav>
</header>

<section class="hero">
  <div class="hero-photo" role="img" aria-label="Two smiling women holding yoga mats in front of a marble wall"></div>
  <div class="hero-content">
    <h1 class="hero-title">Helping people feel <em>more at home</em> in their bodies.</h1>
    <p class="hero-lead">Through touch, movement and education, I support people in exploring their bodies with curiosity, awareness and possibility.</p>
    <div class="hero-actions">
      <a class="btn btn-primary" href="#">Book a session</a>
      <a class="btn btn-ghost" href="#">Discover Kavenda®</a>
    </div>
  </div>
</section>

<section class="pathways">
  <article class="pathway pathway-bodywork">
    <div class="pathway-image img-touch" role="img" aria-label="Hands resting on a client's back during a bodywork session"></div>
    <h2>Kavenda®</h2>
    <p>Structural Integration through intelligent touch. We work together to reorganize the connective tissue, allowing for better alignment and ease of movement.</p>
    <ul><li>Touch &amp; Release</li><li>Structural Alignment</li><li>Deep Awareness</li></ul>
    <a class="text-link" href="#">Learn more about the 10-series
      <svg width="14" height="12" viewBox="0 0 14 12"><path d="M1 6h11M7 1l5 5-5 5" fill="none" stroke="currentColor" stroke-width="1.6"/></svg></a>
  </article>
  <article class="pathway pathway-movement">
    <div class="pathway-image img-studio" role="img" aria-label="Dancer balancing in a sunlit wooden studio with tall windows"></div>
    <h2>Movement &amp; Education</h2>
    <p>Integrating Pilates, Yoga, and functional anatomy to build a resilient, communicative body. Workshops and private sessions designed for lasting change.</p>
    <ul><li>Functional Pilates</li><li>Integrative Yoga</li><li>Anatomy Workshops</li></ul>
    <a class="text-link" href="#">Explore workshops
      <svg width="14" height="12" viewBox="0 0 14 12"><path d="M1 6h11M7 1l5 5-5 5" fill="none" stroke="currentColor" stroke-width="1.6"/></svg></a>
  </article>
</section>

<section class="about">
  <div class="about-portrait" role="img" aria-label="Portrait of the practitioner seated on a mat in a warm, sunlit studio"></div>
  <div class="about-text">
    <span class="eyebrow">About</span>
    <h2>Guided by Curiosity and Care</h2>
    <p>I am Liesbet, a certified Kavenda™ practitioner and movement educator based in Europe. My journey into structural integration began with a fascination for the architecture of the human body and how our physical patterns shape our experience of the world.</p>
    <p>My practice is dedicated to helping you find more space, more ease, and a deeper connection to your physical self. Whether you are recovering from injury or simply looking to move more freely, I provide the tools and guidance for your personal exploration.</p>
    <a class="btn btn-outline" href="#">Read my story</a>
  </div>
</section>

<section class="events">
  <span class="events-label">CONTINUING EDUCATION</span>
  <div class="events-head">
    <h2>Upcoming Events</h2>
    <a class="view-all" href="#">View all events &nbsp;›</a>
  </div>
  <div class="event-grid">
    <article class="event-card">
      <div class="event-image img-workshop" role="img" aria-label="Group of students practising on mats with blocks in a bright studio"></div>
      <div class="event-meta"><span class="badge badge-workshop">Workshop</span>Oct 24, 2024</div>
      <h3>Breath as Architecture</h3>
      <p>A weekend exploration of the diaphragm and thoracic mobility in Brussels.</p>
      <a class="event-status" href="#">Registration open</a>
    </article>
    <article class="event-card">
      <div class="event-image img-retreat" role="img" aria-label="Green rolling hills at dusk beside a stone retreat house"></div>
      <div class="event-meta"><span class="badge badge-retreat">Retreat</span>Nov 12-15, 2024</div>
      <h3>Grounded Presence</h3>
      <p>Four days of intensive Kavenda principles and movement in the Swiss Alps.</p>
      <a class="event-status" href="#">Only 2 spots left</a>
    </article>
    <article class="event-card">
      <div class="event-image img-course" role="img" aria-label="Open anatomy book, tablet and coffee cup on a mint table"></div>
      <div class="event-meta"><span class="badge badge-course">Online course</span>On-Demand</div>
      <h3>Anatomy of Ease</h3>
      <p>A digital deep-dive into the pelvic floor and spinal integrity for movement teachers.</p>
      <a class="event-status" href="#">Learn more</a>
    </article>
  </div>
</section>

<section class="connect">
  <div class="newsletter">
    <h2>Stay Connected</h2>
    <p>Receive occasional insights on movement, anatomy, and upcoming workshops. No spam, just curiosity.</p>
    <form class="subscribe">
      <input type="email" placeholder="Your email address" aria-label="Your email address">
      <button type="button">SUBSCRIBE</button>
    </form>
  </div>
  <div class="contact-card">
    <h3>Have a question?</h3>
    <p>I am always happy to discuss how Kavenda® or movement education might support your specific needs.</p>
    <ul class="contact-list">
      <li><svg width="16" height="12" viewBox="0 0 16 12"><rect x="1" y="1" width="14" height="10" fill="none" stroke="#d07b5a" stroke-width="1.4"/><path d="M1 1l7 5 7-5" fill="none" stroke="#d07b5a" stroke-width="1.4"/></svg>hello@liesbetoonwerk.example</li>
      <li><svg width="16" height="16" viewBox="0 0 16 16"><path d="M8 15s5-5 5-9a5 5 0 0 0-10 0c0 4 5 9 5 9z" fill="none" stroke="#d07b5a" stroke-width="1.4"/><circle cx="8" cy="6" r="1.8" fill="none" stroke="#d07b5a" stroke-width="1.4"/></svg>Brussels &amp; Gent, Belgium</li>
    </ul>
    <div class="social"><span aria-label="Social profile"></span><span aria-label="Social profile"></span></div>
  </div>
</section>

<footer class="site-footer">
  <div class="footer-brand">
    <a class="brand" href="#"><span class="brand-dot"></span>Liesbet Oonwerk</a>
    <p>Structural Integration &amp;<br>Movement Education.</p>
  </div>
  <div class="footer-col footer-pages">
    <h4>PAGES</h4>
    <ul><li>Kavenda®</li><li>Movement</li><li>Education</li><li>About</li><li>Contact</li></ul>
  </div>
  <div class="footer-col footer-locations">
    <h4>LOCATIONS</h4>
    <ul><li>Studio Lindeplein Movement</li><li>Lab Gent Belgium</li></ul>
  </div>
  <p class="copyright">© 2024 Liesbet Oonwerk. All rights reserved. Kavenda®</p>
</footer>

</body>
</html>
```